Brightfold Partners Website

Brightfold Partners (BP) provide Analytics & Enterprise Performance Management (EPM) advisory & consultancy services. We are passionate about data and making a difference for our clients by working in partnership with them, helping them on their journey to becoming an Brightfold Partner. We deliver insights which give our clients a competitive edge and a much deeper understanding of their organisation.

We need a website which shows who we are, what we do and how we do it.

www.brightfold-partners.example is our very basic website at the moment. We want to completely revamp it with a corporate look

```html
<!DOCTYPE html>
<html lang="en">
<head>
<meta charset="utf-8">
<title>Brightfold Partners</title>
<link rel="stylesheet" href="https://fonts.googleapis.com/css2?family=Montserrat:wght@400;500;600;700;800&family=Open+Sans:wght@400;600&display=swap">
<style>
:root{
  --navy:#102536;
  --deep:#173a52;
  --blue:#245675;
  --steel:#3d6f8e;
  --ice:#dfe8ef;
  --ink:#1d2a33;
  --grey:#6b7780;
  --white:#ffffff;
}
*{margin:0;padding:0;box-sizing:border-box}
html,body{width:1200px;height:2684px;overflow:hidden;background:var(--white)}
body{font-family:"Open Sans",Arial,sans-serif;color:var(--ink);position:relative}
.abs{position:absolute}
.heading{font-family:"Montserrat",Arial,sans-serif}

.topbar{left:0;top:0;width:1200px;height:22px;background:var(--navy);color:var(--white);font-size:11px;display:flex;justify-content:center;align-items:center;gap:28px}
.topbar span{display:flex;align-items:center;gap:6px}

.nav{left:0;top:22px;width:1200px;height:48px;background:var(--deep);display:flex;align-items:center;padding:0 40px}
.brand{display:flex;align-items:center;gap:10px;color:var(--white);font-family:"Montserrat",Arial,sans-serif;font-weight:700;font-size:15px;letter-spacing:.5px;text-transform:uppercase;line-height:1.05;width:230px}
.brand .dot{width:26px;height:26px;border-radius:50%;background:var(--white)}
.menu{display:flex;margin-left:20px}
.menu a{color:var(--white);text-decoration:none;font-family:"Montserrat",Arial,sans-serif;font-size:12px;font-weight:500;padding:0 30px;border-right:1px solid rgba(255,255,255,.35);line-height:48px}
.menu a.active{background:rgba(255,255,255,.08)}
.menu a:last-child{border-right:none}
.social-top{margin-left:auto;display:flex;gap:6px}
.social-top i{width:24px;height:24px;border-radius:6px;background:var(--ice);display:block}

.hero{left:0;top:70px;width:1200px;height:790px;overflow:hidden}
.hero-photo{position:absolute;inset:0;background:radial-gradient(ellipse at 25% 45%,#5f8aa8 0%,#2d5b7a 35%,#14324a 75%),#14324a}
.hero-text{position:absolute;right:150px;top:220px;width:440px;text-align:center;color:var(--white)}
.hero-text h1{font-family:"Montserrat",Arial,sans-serif;font-weight:800;font-size:40px;line-height:1.1}
.hero-text h2{font-family:"Montserrat",Arial,sans-serif;font-weight:700;font-size:21px;line-height:1.25;margin-top:18px}
.btn{display:inline-block;font-family:"Montserrat",Arial,sans-serif;font-size:11px;font-weight:600;color:var(--white);border:1px solid var(--white);background:var(--blue);padding:10px 18px;letter-spacing:.5px}
.hero-text .btn{margin-top:24px}
.arrow{position:absolute;top:400px;color:var(--white);font-size:18px}
.wave{position:absolute;left:0;bottom:0}
.dots{position:absolute;left:0;width:1200px;bottom:32px;display:flex;justify-content:center;gap:8px}
.dots i{width:8px;height:8px;border-radius:50%;background:#b7c3cc;display:block}
.dots i.on{background:var(--steel)}

.section-title{left:0;width:1200px;text-align:center;font-family:"Montserrat",Arial,sans-serif;font-size:34px;color:var(--ink);font-weight:400;letter-spacing:1px}
.section-title b{font-weight:800}
.section-title::after{content:"";display:block;width:60px;height:2px;background:var(--steel);margin:10px auto 0}

.card{top:1000px;width:280px;height:330px}
.card-photo{width:280px;height:140px;border-radius:22px 22px 0 0}
.card-icon{position:absolute;left:115px;top:112px;width:50px;height:50px;border-radius:50%;background:var(--deep);border:3px solid var(--white);display:flex;align-items:center;justify-content:center}
.card h3{font-family:"Montserrat",Arial,sans-serif;font-size:15px;font-weight:700;text-align:center;margin-top:34px}
.card p{font-size:11px;color:var(--grey);text-align:center;line-height:1.55;padding:8px 26px 0}
.card .more{display:block;text-align:center;font-family:"Montserrat",Arial,sans-serif;font-size:10px;color:var(--blue);font-weight:600;margin-top:12px}

.about-photo{left:150px;top:1430px;width:560px;height:430px;border-radius:70px 0 70px 0;background:linear-gradient(135deg,#dfe5ea,#9fb2c0 60%,#6c879b)}
.about-text{left:745px;top:1520px;width:300px;font-size:12px;line-height:1.6;color:var(--ink)}
.about-btn{left:850px;top:1785px;background:var(--deep);border-color:var(--deep);padding:12px 20px}

.contact{left:0;top:1890px;width:1200px;height:330px;background:linear-gradient(90deg,#0f2232,#1e4560 60%,#163448)}
.contact h2{position:absolute;left:150px;top:95px;width:460px;text-align:center;color:var(--white);font-family:"Montserrat",Arial,sans-serif;font-size:30px;font-weight:400;line-height:1.15}
.contact h2 b{font-weight:800}
.contact .lead{position:absolute;left:150px;top:190px;width:460px;text-align:center;color:var(--white);font-family:"Montserrat",Arial,sans-serif;font-size:13px;font-weight:600}
.contact-actions{position:absolute;left:195px;top:233px;display:flex;align-items:center;border:1px solid rgba(255,255,255,.6);border-radius:8px;height:36px}
.contact-actions span{color:var(--white);font-family:"Montserrat",Arial,sans-serif;font-size:10px;font-weight:600;padding:0 26px;display:flex;align-items:center;gap:6px}
.contact-actions .or{width:32px;height:32px;border-radius:50%;background:var(--white);color:var(--deep);padding:0;justify-content:center}
.contact-photo{position:absolute;left:720px;top:100px;width:330px;height:215px;border-radius:40px 0 40px 0;background:linear-gradient(135deg,#f2f4f6,#c4cfd8 55%,#8ea3b3)}

.footer-brand{left:70px;top:2330px;width:200px}
.footer-brand .brand{color:var(--deep);width:auto}
.footer-brand .brand .dot{background:var(--deep)}
.footer-brand p{font-size:11px;color:var(--grey);line-height:1.55;margin-top:14px}
.footer-col h4{font-family:"Montserrat",Arial,sans-serif;font-size:13px;font-weight:700;color:var(--ink);padding-bottom:6px;border-bottom:2px solid var(--steel);display:inline-block}
.footer-col ul{list-style:none;margin-top:22px}
.footer-col li{font-size:11px;line-height:1;margin-bottom:18px;color:var(--ink);display:flex;gap:8px;align-items:flex-start}
.follow{font-size:11px;color:var(--grey);margin-top:22px}
.social-foot{display:flex;gap:8px;margin-top:14px}
.social-foot i{width:30px;height:30px;border-radius:6px;background:var(--deep);display:block}
.copyright{left:0;top:2650px;width:1200px;height:34px;background:var(--navy);color:var(--white);font-size:10px;display:flex;align-items:center;justify-content:center}
</style>
</head>
<body>

<div class="abs topbar">
  <span><svg width="9" height="12" viewBox="0 0 9 12"><path d="M4.5 0A4.5 4.5 0 0 0 0 4.5C0 8 4.5 12 4.5 12S9 8 9 4.5A4.5 4.5 0 0 0 4.5 0Zm0 6.3a1.8 1.8 0 1 1 0-3.6 1.8 1.8 0 0 1 0 3.6Z" fill="#fff"/></svg>12 Harbour Row, Dublin 2, D02 AB12</span>
  <span><svg width="11" height="11" viewBox="0 0 24 24"><path d="M6.6 10.8a15 15 0 0 0 6.6 6.6l2.2-2.2a1 1 0 0 1 1-.25 11.4 11.4 0 0 0 3.6.57 1 1 0 0 1 1 1V20a1 1 0 0 1-1 1A17 17 0 0 1 3 4a1 1 0 0 1 1-1h3.5a1 1 0 0 1 1 1c0 1.25.2 2.45.57 3.57a1 1 0 0 1-.25 1Z" fill="#fff"/></svg>01 555 0142</span>
</div>

<nav class="abs nav">
  <div class="brand"><span class="dot"></span><span>Brightfold<br>Partners</span></div>
  <div class="menu">
    <a class="active">HOME</a><a>ABOUT US</a><a>SERVICES ▾</a><a>CONTACT US</a>
  </div>
  <div class="social-top"><i></i><i></i></div>
</nav>

<section class="abs hero">
  <div class="hero-photo" role="img" aria-label="Hands holding a tablet with glowing data analytics dashboards and charts"></div>
  <span class="arrow" style="left:8px">❮</span>
  <span class="arrow" style="right:8px">❯</span>
  <div class="hero-text">
    <h1>WELCOME TO<br>Brightfold Partners</h1>
    <h2>WE ARE THE BEST DATA ANALYTICS &amp; EPM CONSULTING SERVICES PROVIDER</h2>
    <span class="btn">EXPLORE OUR SERVICES</span>
  </div>
  <svg class="wave" width="1200" height="120" viewBox="0 0 1200 120"><path d="M0 40 C300 110 700 110 1200 20 L1200 120 L0 120 Z" fill="#fff"/></svg>
  <div class="dots"><i></i><i class="on"></i><i></i></div>
</section>

<h2 class="abs section-title" style="top:895px">OUR <b>SERVICES</b></h2>

<div class="abs card" style="left:145px">
  <div class="card-photo" role="img" aria-label="Colleagues meeting around a laptop" style="background:linear-gradient(135deg,#c9d3da,#7f97a8)"></div>
  <div class="card-icon"><svg width="22" height="22" viewBox="0 0 24 24"><rect x="4" y="12" width="3" height="8" fill="#fff"/><rect x="10.5" y="7" width="3" height="13" fill="#fff"/><rect x="17" y="4" width="3" height="16" fill="#fff"/></svg></div>
  <h3>Advise &amp; Architect</h3>
  <p>Helping our customers understand their data and build a roadmap that delivers real value from every investment.</p>
  <span class="more">LEARN MORE ❯</span>
</div>

<div class="abs card" style="left:460px">
  <div class="card-photo" role="img" aria-label="Team collaborating over printed charts" style="background:linear-gradient(135deg,#b9c4cc,#6d8597)"></div>
  <div class="card-icon"><svg width="22" height="22" viewBox="0 0 24 24"><path d="M4 20h16M6 16l4-5 4 3 5-7" stroke="#fff" stroke-width="2" fill="none"/></svg></div>
  <h3>Design &amp; Implement</h3>
  <p>Working with the project team through each stage to design and implement solutions that meet business needs.</p>
  <span class="more">LEARN MORE ❯</span>
</div>

<div class="abs card" style="left:775px">
  <div class="card-photo" role="img" aria-label="Consultant reviewing charts on a desk" style="background:linear-gradient(135deg,#d3dbe1,#8aa0b0)"></div>
  <div class="card-icon"><svg width="22" height="22" viewBox="0 0 24 24"><circle cx="12" cy="12" r="4" stroke="#fff" stroke-width="2" fill="none"/><circle cx="12" cy="12" r="8.5" stroke="#fff" stroke-width="2" stroke-dasharray="3 2.5" fill="none"/></svg></div>
  <h3>Optimise &amp; Manage</h3>
  <p>Our managed service delivers proactive, on-demand support for EPM and data analytics environments.</p>
  <span class="more">LEARN MORE ❯</span>
</div>

<h2 class="abs section-title" style="top:1345px">ABOUT <b>US</b></h2>

<div class="abs about-photo" role="img" aria-label="Businesswoman presenting a bar chart on a screen"></div>
<p class="abs about-text">Brightfold Partner is an exciting start up in the Data Analytics and EPM space. Founded in 2019, BP specialise in the implementation and support of BP EPM and Data Analytics business solutions, both in the Cloud and on-premise.</p>
<span class="abs btn about-btn">EXPLORE MORE ❯</span>

<section class="abs contact">
  <h2>CONTACT US TO DISCUSS<br><b>YOUR BUSINESS NEEDS</b></h2>
  <p class="lead">WE LOVE TO HEAR FROM YOU!</p>
  <div class="contact-actions">
    <span><svg width="10" height="10" viewBox="0 0 24 24"><path d="M6.6 10.8a15 15 0 0 0 6.6 6.6l2.2-2.2a1 1 0 0 1 1-.25 11.4 11.4 0 0 0 3.6.57 1 1 0 0 1 1 1V20a1 1 0 0 1-1 1A17 17 0 0 1 3 4a1 1 0 0 1 1-1h3.5a1 1 0 0 1 1 1c0 1.25.2 2.45.57 3.57a1 1 0 0 1-.25 1Z" fill="#fff"/></svg>CALL US 01 555 0142</span>
    <span class="or">OR</span>
    <span><svg width="11" height="9" viewBox="0 0 22 16"><rect x="1" y="1" width="20" height="14" fill="none" stroke="#fff" stroke-width="2"/><path d="M1 1l10 8 10-8" fill="none" stroke="#fff" stroke-width="2"/></svg>CONTACT US</span>
  </div>
  <div class="contact-photo" role="img" aria-label="Professional working at a laptop in a bright office"></div>
</section>

<div class="abs footer-brand">
  <div class="brand"><span class="dot"></span><span>Brightfold<br>Partners</span></div>
  <p>BP are a Data Analytics &amp; EPM company, specialising in the implementation and support of Business Intelligence, EPM and Data Analytics business solutions, both in the Cloud and on-premise.</p>
</div>

<div class="abs footer-col" style="left:390px;top:2335px">
  <h4>LINKS</h4>
  <ul><li>HOME</li><li>ABOUT US</li><li>SERVICES ▾</li><li>CONTACT US</li></ul>
</div>

<div class="abs footer-col" style="left:625px;top:2335px">
  <h4>CONTACT US</h4>
  <ul>
    <li><svg width="10" height="13" viewBox="0 0 9 12"><path d="M4.5 0A4.5 4.5 0 0 0 0 4.5C0 8 4.5 12 4.5 12S9 8 9 4.5A4.5 4.5 0 0 0 4.5 0Z" fill="#173a52"/></svg><span style="line-height:1.4">12 Harbour Row,<br>Dublin 2, D02 AB12</span></li>
    <li><svg width="11" height="11" viewBox="0 0 24 24"><path d="M6.6 10.8a15 15 0 0 0 6.6 6.6l2.2-2.2a1 1 0 0 1 1-.25 11.4 11.4 0 0 0 3.6.57 1 1 0 0 1 1 1V20a1 1 0 0 1-1 1A17 17 0 0 1 3 4a1 1 0 0 1 1-1h3.5a1 1 0 0 1 1 1c0 1.25.2 2.45.57 3.57a1 1 0 0 1-.25 1Z" fill="#173a52"/></svg>01 555 0142</li>
  </ul>
</div>

<div class="abs footer-col" style="left:890px;top:2335px">
  <h4>SOCIAL MEDIA</h4>
  <p class="follow">FOLLOW OUR SOCIAL MEDIA</p>
  <div class="social-foot"><i></i><i></i></div>
</div>

<div class="abs copyright">Copyright © 2022 Brightfold Partners | Powered by Brightfold Partners</div>

</body>
</html>
```